out of the box Business Card Design for a Manufacturer / Distributor

We are a manufarturer and distributor of products.
the company name is VORTANI (Pic attached)

the picture is NOT a must have on the business Card.

the Business Card should look really professional and/or special, so out of the box thinking is welcome.

there should be 2 Adresses on the Business Card for Main and Branch Office.
Email Adress, homepage, Name is required
NO Phone Number

Our working field:
Private Labeling
high Quality Production
direct distribution
warehousing
trademark registration
legal support

Main Office:
Kornblumenweg 14
08352 Eschenthal
Westmark

Branch Office:
Daska Lane
Rivabad
Eastvale

Names:
Lukas Feldhaus (Owner)
Imran Qureshi (Owner)

Email:
lukas@vortani-example.com
imran@vortani-example.com

homepage:
vortani-example.com

Industry/Entity Type

Manufacturer Distributer

Contact Information for Business Card

Vortani

Requirements
Must have
• Names, both office Adresses, email, homepage
Should not have
• Phone Number

```html
<!DOCTYPE html>
<html lang="en">
<head>
<meta charset="utf-8">
<title>Vortani Business Card</title>
<link rel="stylesheet" href="https://fonts.googleapis.com/css2?family=Roboto:wght@300;400;500;700&display=swap">
<style>
  :root {
    --stage-light: #efefef;
    --stage-dark: #d4d4d4;
    --front-light: #7d7d7d;
    --front-mid: #5b5c5c;
    --front-dark: #3a3b3b;
    --back-light: #3f4040;
    --back-dark: #2a2b2b;
    --ink: #ffffff;
    --ink-soft: #e6e6e6;
    --accent-front: #b6b3b1;
    --accent-back: #8a8784;
  }
  * { box-sizing: border-box; margin: 0; padding: 0; }
  html, body { width: 1200px; height: 805px; overflow: hidden; }
  body {
    position: relative;
    font-family: "Roboto", Arial, sans-serif;
    color: var(--ink);
    background: linear-gradient(135deg, var(--stage-light) 0%, var(--stage-dark) 100%);
  }
  .card {
    position: absolute;
    width: 527px;
    height: 322px;
    overflow: hidden;
  }
  .card--front {
    left: 145px; top: 65px;
    background: linear-gradient(60deg, var(--front-light) 0%, var(--front-mid) 40%, var(--front-dark) 100%);
  }
  .card--back {
    left: 528px; top: 416px;
    background: linear-gradient(90deg, var(--back-light) 0%, var(--back-dark) 100%);
  }
  .abs { position: absolute; white-space: nowrap; }

  .brand-dot {
    position: absolute;
    width: 28px; height: 28px;
    border-radius: 50%;
    background: var(--ink);
  }
  .brand-name {
    position: absolute;
    font-size: 38px;
    font-weight: 400;
    letter-spacing: 0.5px;
    line-height: 1;
    white-space: nowrap;
  }

  .person-name { left: 29px; top: 33px; font-size: 21px; font-weight: 700; }
  .person-role { left: 31px; top: 59px; font-size: 14px; font-weight: 400; color: var(--ink-soft); }

  .contact-line {
    position: absolute;
    left: 30px;
    width: 152px;
    padding-bottom: 5px;
    border-bottom: 1px solid var(--ink-soft);
    font-size: 13.5px;
    display: flex;
    align-items: center;
    gap: 4px;
    white-space: nowrap;
  }
  .contact-line svg { flex: none; }
  .contact-line--email { top: 95px; }
  .contact-line--web { top: 126px; }

  .services { position: absolute; left: 291px; top: 137px; list-style: none; }
  .services li {
    display: flex; align-items: center; gap: 10px;
    height: 27px;
    font-size: 18.5px; font-weight: 300;
    white-space: nowrap;
  }

  .decor {
    position: absolute;
    border-radius: 50%;
  }
  .decor--front { left: -12px; top: 237px; width: 170px; height: 170px; background: var(--accent-front); }
  .decor--back { left: 354px; top: 182px; width: 160px; height: 160px; background: var(--accent-back); }

  .back-web {
    position: absolute; left: 64px; top: 139px; width: 151px;
    padding-left: 2px; padding-bottom: 5px;
    border-bottom: 1px solid var(--ink-soft);
    font-size: 13.5px; white-space: nowrap;
  }
  .office { position: absolute; top: 214px; }
  .office--main { left: 60px; }
  .office--branch { left: 239px; top: 216px; }
  .office-title {
    display: inline-block;
    font-size: 14px; font-weight: 500;
    padding-bottom: 3px;
    position: relative;
  }
  .office-title::after {
    content: ""; position: absolute; left: 0; bottom: 0;
    width: 42px; height: 1px; background: var(--ink-soft);
  }
  .office-address { margin-top: 8px; font-size: 14px; line-height: 16px; font-style: normal; white-space: nowrap; }
  .office--branch .office-address { margin-top: 6px; }
</style>
</head>
<body>

  <section class="card card--front" aria-label="Business card front">
    <div class="decor decor--front"></div>

    <div class="abs person-name">Lukas Feldhaus</div>
    <div class="abs person-role">Owner</div>

    <div class="contact-line contact-line--email">
      <svg width="12" height="10" viewBox="0 0 12 10" aria-hidden="true"><rect x="0.6" y="0.6" width="10.8" height="8.8" rx="1.5" fill="none" stroke="#fff" stroke-width="1.1"/><path d="M1 1.5 L6 5.5 L11 1.5" fill="none" stroke="#fff" stroke-width="1.1"/></svg>
      <span>lukas@vortani-example.com</span>
    </div>
    <div class="contact-line contact-line--web">
      <svg width="11" height="11" viewBox="0 0 12 12" aria-hidden="true"><circle cx="6" cy="6" r="5.2" fill="none" stroke="#fff" stroke-width="1.1"/><path d="M1 6 H11 M6 1 C3 4 3 8 6 11 M6 1 C9 4 9 8 6 11" fill="none" stroke="#fff" stroke-width="1"/></svg>
      <span>www.vortani-example.com</span>
    </div>

    <div class="brand-dot" style="left:284px; top:39px;"></div>
    <div class="brand-name" style="left:328px; top:40px;">VORTANI</div>

    <ul class="services">
      <li><svg width="13" height="13" viewBox="0 0 14 14" aria-hidden="true"><path d="M12.5 7 A5.5 5.5 0 1 1 9.5 2.1" fill="none" stroke="#fff" stroke-width="1.2"/><path d="M4.5 6.8 L6.6 8.8 L12 3.2" fill="none" stroke="#fff" stroke-width="1.3"/></svg>Private Labeling</li>
      <li><svg width="13" height="13" viewBox="0 0 14 14" aria-hidden="true"><path d="M12.5 7 A5.5 5.5 0 1 1 9.5 2.1" fill="none" stroke="#fff" stroke-width="1.2"/><path d="M4.5 6.8 L6.6 8.8 L12 3.2" fill="none" stroke="#fff" stroke-width="1.3"/></svg>High Quality Production</li>
      <li><svg width="13" height="13" viewBox="0 0 14 14" aria-hidden="true"><path d="M12.5 7 A5.5 5.5 0 1 1 9.5 2.1" fill="none" stroke="#fff" stroke-width="1.2"/><path d="M4.5 6.8 L6.6 8.8 L12 3.2" fill="none" stroke="#fff" stroke-width="1.3"/></svg>Direct distribution</li>
      <li><svg width="13" height="13" viewBox="0 0 14 14" aria-hidden="true"><path d="M12.5 7 A5.5 5.5 0 1 1 9.5 2.1" fill="none" stroke="#fff" stroke-width="1.2"/><path d="M4.5 6.8 L6.6 8.8 L12 3.2" fill="none" stroke="#fff" stroke-width="1.3"/></svg>Warehousing</li>
      <li><svg width="13" height="13" viewBox="0 0 14 14" aria-hidden="true"><path d="M12.5 7 A5.5 5.5 0 1 1 9.5 2.1" fill="none" stroke="#fff" stroke-width="1.2"/><path d="M4.5 6.8 L6.6 8.8 L12 3.2" fill="none" stroke="#fff" stroke-width="1.3"/></svg>Trademark registration</li>
      <li><svg width="13" height="13" viewBox="0 0 14 14" aria-hidden="true"><path d="M12.5 7 A5.5 5.5 0 1 1 9.5 2.1" fill="none" stroke="#fff" stroke-width="1.2"/><path d="M4.5 6.8 L6.6 8.8 L12 3.2" fill="none" stroke="#fff" stroke-width="1.3"/></svg>Legal support</li>
    </ul>
  </section>

  <section class="card card--back" aria-label="Business card back">
    <div class="decor decor--back"></div>

    <div class="brand-dot" style="left:56px; top:61px;"></div>
    <div class="brand-name" style="left:106px; top:62px;">VORTANI</div>

    <div class="back-web">www.vortani-example.com</div>

    <div class="office office--main">
      <div class="office-title">Main Office</div>
      <address class="office-address">Kornblumenweg 14<br>08352 Eschenthal<br>Westmark</address>
    </div>
    <div class="office office--branch">
      <div class="office-title">Branch Office</div>
      <address class="office-address">Daska Lane<br>Rivabad<br>Eastvale</address>
    </div>
  </section>

</body>
</html>
```